Business Card for a mobile physiotherapy company

I need a layout for a business card for a mobile physiotherapy company.
Slogan is "Mobile Physiotherapy - Your Road To Recovery"
Phone number is 867-402-5913
Email VantrePhysio@mailbright.ca (subject to change with website)
Website www.VantrePhysio.ca
My name and credentials: Kent Vantre Kent Vantre, BSc(kin), MPT, CAFCI, IMS
Information maybe included: Direct Billing, Services including Physiotherapy, IMS, acupuncture
Maybe include facebook and instagram logos
One side with the logo clean and sharp
Other side with details, try not to look too busy, keep everything concise

```html
<!DOCTYPE html>
<html lang="en">
<head>
<meta charset="UTF-8">
<title>Vantre Physio – Business Card</title>
<link href="https://fonts.googleapis.com/css2?family=Libre+Baskerville:wght@700&family=Open+Sans:wght@400;600;700&display=swap" rel="stylesheet">
<style>
  :root {
    --stage: #232323;
    --navy: #2b4a78;
    --navy-light: #4d6a92;
    --navy-deep: #27446d;
    --green: #0f5a4c;
    --ink: #1d1d1d;
    --paper: #ffffff;
  }
  * { margin: 0; padding: 0; box-sizing: border-box; }
  html, body { width: 1200px; height: 895px; overflow: hidden; background: var(--stage); }
  body { position: relative; font-family: "Open Sans", Arial, sans-serif; }

  .card {
    position: absolute;
    left: 320px;
    width: 560px;
    height: 320px;
    border-radius: 22px;
    overflow: hidden;
    box-shadow: 0 10px 30px rgba(0,0,0,.5);
  }

  /* Front */
  .card-front {
    top: 100px;
    background: radial-gradient(ellipse at 45% 40%, var(--navy-light) 0%, var(--navy-deep) 70%);
    color: var(--paper);
    text-align: center;
  }
  .front-brand {
    margin-top: 92px;
    display: flex; align-items: center; justify-content: center; gap: 14px;
  }
  .brand-mark { width: 22px; height: 22px; background: currentColor; }
  .brand-name {
    font-family: "Open Sans", Arial, sans-serif;
    font-weight: 700;
    font-size: 44px;
    letter-spacing: 4px;
    line-height: 1;
  }
  .front-slogan { margin-top: 26px; font-size: 15px; font-weight: 600; letter-spacing: .4px; }
  .front-social {
    margin-top: 14px;
    display: flex; align-items: center; justify-content: center; gap: 8px;
    font-size: 14px;
  }
  .social-dot { width: 14px; height: 14px; border-radius: 50%; background: var(--paper); }

  /* Back */
  .card-back { top: 470px; background: var(--paper); color: var(--ink); }
  .back-brand {
    position: absolute; left: 36px; top: 100px;
    display: flex; align-items: center; gap: 10px;
    color: var(--navy);
  }
  .back-brand .brand-mark { width: 16px; height: 16px; }
  .back-brand .brand-name { font-size: 30px; letter-spacing: 2px; }

  .holder {
    position: absolute; left: 300px; top: 40px;
    padding-left: 16px; border-left: 1.5px solid var(--green);
  }
  .holder-name {
    font-family: "Libre Baskerville", Georgia, serif;
    font-weight: 700; font-size: 24px; color: var(--navy); letter-spacing: -.5px;
  }
  .holder-credentials { font-size: 14px; color: var(--green); margin-top: 2px; }

  .contact-list {
    position: absolute; left: 300px; top: 136px;
    padding-left: 16px; border-left: 1.5px solid var(--navy);
    list-style: none; font-size: 14px; line-height: 22px;
  }
  .contact-list li { display: flex; align-items: center; gap: 8px; }
  .contact-icon { width: 12px; height: 12px; flex: none; color: var(--green); }

  .services {
    position: absolute; left: 0; right: 0; bottom: 30px;
    text-align: center; font-size: 14px; letter-spacing: .2px;
  }
  .services .sep { margin: 0 8px; }

  .band { position: absolute; left: 0; right: 0; bottom: 0; height: 10px; display: flex; }
  .band-navy { flex: 1; background: var(--navy); }
  .band-green { flex: 1; background: var(--green); }
</style>
</head>
<body>

<section class="card card-front">
  <div class="front-brand">
    <span class="brand-mark"></span>
    <span class="brand-name">VANTRE PHYSIO</span>
  </div>
  <p class="front-slogan">Mobile Physiotherapy - Your Road To Recovery</p>
  <p class="front-social"><span class="social-dot"></span>VantrePhysio</p>
</section>

<section class="card card-back">
  <div class="back-brand">
    <span class="brand-mark"></span>
    <span class="brand-name">VANTRE PHYSIO</span>
  </div>

  <div class="holder">
    <h1 class="holder-name">KENT VANTRE</h1>
    <p class="holder-credentials">BSc(kin), MPT, CAFCI, IMS</p>
  </div>

  <ul class="contact-list">
    <li>
      <svg class="contact-icon" viewBox="0 0 24 24"><path fill="currentColor" d="M6.6 10.8a15.1 15.1 0 0 0 6.6 6.6l2.2-2.2c.3-.3.7-.4 1-.2 1.1.4 2.3.6 3.6.6.6 0 1 .4 1 1V20c0 .6-.4 1-1 1A17 17 0 0 1 3 4c0-.6.4-1 1-1h3.5c.6 0 1 .4 1 1 0 1.3.2 2.5.6 3.6.1.3 0 .7-.2 1z"/></svg>
      867-402-5913
    </li>
    <li>
      <svg class="contact-icon" viewBox="0 0 24 24"><path fill="currentColor" d="M2 5h20v14H2z"/><path fill="none" stroke="#fff" stroke-width="2" d="M2 5l10 8 10-8"/></svg>
      VantrePhysio@mailbright.ca
    </li>
    <li>
      <svg class="contact-icon" viewBox="0 0 24 24"><g fill="none" stroke="currentColor" stroke-width="2"><circle cx="12" cy="12" r="10"/><path d="M2 12h20M12 2c3 3 3 17 0 20M12 2c-3 3-3 17 0 20"/></g></svg>
      www.VantrePhysio.ca
    </li>
  </ul>

  <p class="services">Direct Billing<span class="sep">|</span>Services including Physiotherapy<span class="sep">|</span>IMS<span class="sep">|</span>Acupuncture</p>

  <div class="band"><span class="band-navy"></span><span class="band-green"></span></div>
</section>

</body>
</html>
```